EdTech startup needs web (& logo?) redesign

LecternHop.com is a collection of fun online tools designed to help instructors in higher education (i.e. university) build a sense of community in the classroom and enable "active learning." We have spent most of our energy on developing functionality and would love to have some real designers contribute their ideas. Everything (logos, color scheme, images, etc.) is up for grabs, but the winning design should be bootstrap friendly. We are currently using the "Megaframe" template, but are open to others. That being said, we are less interested in getting great code than a great design. Websites we admire include voteswirl.com, workmesh.com, and http://skins.fetchframe.com/products/application

Pages we are particularly interested in ideas for include: homepage, shuffle pick, the grabber, and extra tambourine. The latter three currently use images that probably can't go mainstream.

If you want to participate in the contest we would love for you to check out the site first. In order to enable this, we have set up a fictional class (LPHX 207-3 - Beta Website Redesign). Once you create an account at www.lecternhop.com, you just enter the super-secret invite code "e9a27b41" to add yourself to the class.

Attached our some files that were used to inspire our current design. Feel free to use or ignore them as you see fit. Thanks!

Target Market(s)

college students and their instructors

Industry/Entity Type

Education

Coding

Coded - Design and coding required

Number of Pages Required

4 page

Colors
0355a3
33a6d7
cee9f5

Requirements
Must have
• cool, fun design that is boostrap friendly.
Nice to have
• I like blue, but an open to other color themes.
Should not have
• ?

```html
<!DOCTYPE html>
<html lang="en">
<head>
<meta charset="utf-8">
<title>LecternHop</title>
<link rel="stylesheet" href="https://fonts.googleapis.com/css2?family=Oswald:wght@300;400&family=Open+Sans:wght@400;600;700&family=Roboto:wght@300;400&display=swap">
<style>
:root{
  --brand:#0355a3;
  --sky:#33a6d7;
  --ice:#cee9f5;
  --ink:#444;
  --white:#fff;
}
*{box-sizing:border-box;margin:0;padding:0}
html,body{width:873px;height:1200px;overflow:hidden;background:var(--white)}
.page{position:relative;width:873px;height:1200px;font-family:"Roboto",sans-serif;color:var(--ink)}
.abs{position:absolute}
.hero{left:0;top:0;width:873px;height:304px;background:
  radial-gradient(ellipse 230px 170px at 560px 190px,#fbfaf8 0%,#f1ece6 45%,rgba(240,200,160,0) 100%),
  radial-gradient(ellipse 260px 200px at 200px 160px,#b58a62 0%,#8a5a3a 60%,rgba(0,0,0,0) 100%),
  linear-gradient(100deg,#7a4a2c 0%,#b06a30 40%,#e07a1c 65%,#d6c2b0 100%)}
.logo{left:182px;top:10px;font-family:"Open Sans",sans-serif;font-size:17px;color:var(--white);font-weight:400}
.nav{right:183px;top:18px;display:flex;gap:10px;font-family:"Open Sans",sans-serif;font-weight:700;font-size:7.2px;color:var(--white)}
.nav .active{border-bottom:2px solid var(--white);padding-bottom:2px}
.welcome{left:430px;top:144px;width:260px;text-align:center}
.welcome h1{font-family:"Oswald",sans-serif;font-weight:400;font-size:13px;color:var(--brand)}
.welcome p{font-size:8.5px;line-height:10px;color:#555;margin-top:6px}
.btn{display:inline-block;background:var(--brand);color:var(--white)}
.welcome .btn{margin-top:9px;width:82px;height:19px;line-height:19px;font-family:"Open Sans",sans-serif;font-size:10px}
.section-title{left:0;width:873px;text-align:center;font-family:"Oswald",sans-serif;font-weight:400;font-size:17px;color:var(--brand)}
.section-title::after{content:"";display:block;width:68px;height:2px;background:var(--sky);margin:3px auto 0}
.intro{left:181px;top:357px;width:510px;text-align:center;font-size:6.6px;line-height:8.4px;color:#666;font-weight:300}
.card{width:123px;height:177px;border:1px solid var(--brand);background:var(--white);text-align:center}
.badge{position:absolute;left:30px;top:-31px;width:62px;height:62px;border-radius:50%;background:var(--ice);border:2px solid var(--brand);border-top-color:var(--ice);border-left-color:var(--ice);display:flex;align-items:center;justify-content:center}
.card h3{margin-top:34px;font-family:"Oswald",sans-serif;font-weight:400;font-size:17px;color:var(--brand);white-space:nowrap}
.card h3.tight{font-size:15px}
.card p{margin:4px 8px 0;font-size:6.9px;line-height:8.4px;color:#444;height:74px}
.card .btn{position:absolute;left:12px;bottom:15px;width:98px;height:18px;line-height:18px;font-family:"Oswald",sans-serif;font-size:8.5px;text-align:center}
.card .btn::after{content:"\00BB";position:absolute;right:7px;font-size:10px}
.band{left:0;top:894px;width:873px;height:176px;background:var(--ice)}
.quote-card{left:181px;top:906px;width:507px;height:140px;background:var(--white);border-bottom-right-radius:40px;box-shadow:2px 2px 4px rgba(0,0,0,.08)}
.quote-card h2{position:absolute;left:0;top:12px;width:100%;text-align:center;font-family:"Oswald",sans-serif;font-weight:400;font-size:15px;color:var(--brand)}
.avatar{left:50px;top:38px;width:77px;height:77px;border-radius:50%;background:radial-gradient(circle at 50% 45%,#d9b49a,#8a2a24 80%)}
.quote-card .name{left:136px;top:44px;font-family:"Oswald",sans-serif;font-weight:300;font-size:8.5px;color:var(--brand)}
.quote-card .text{left:136px;top:68px;width:330px;text-align:center;font-size:8.2px;line-height:10px;color:#555}
.dots{left:426px;top:1056px;display:flex;gap:3px}
.dots span{width:5px;height:4px;background:var(--white)}
.dots span.on{background:var(--brand)}
.foot-title{font-family:"Oswald",sans-serif;font-weight:300;font-size:10px;color:var(--brand)}
.foot-title::after{content:"";display:block;width:96px;height:2px;background:var(--ice);margin-top:3px}
.sitemap{left:189px;top:1101px;list-style:none;font-family:"Oswald",sans-serif;font-weight:300;font-size:6.8px;line-height:10.5px;color:var(--sky)}
.join-lead{left:354px;top:1101px;font-family:"Oswald",sans-serif;font-size:7px;line-height:8.5px;color:var(--brand)}
.email{left:354px;top:1135px;width:95px;height:13px;background:var(--ice);font-size:5px;line-height:13px;padding-left:5px;color:#7aa}
.join-btn{left:354px;top:1152px;width:63px;height:15px;line-height:15px;text-align:center;font-family:"Oswald",sans-serif;font-size:7px}
.contact{left:540px;font-family:"Oswald",sans-serif;font-weight:300;font-size:7px;color:var(--brand);display:flex;align-items:center;gap:7px}
.social{left:540px;top:1151px;display:flex;gap:7px}
.social span{width:20px;height:20px;border-radius:50%;background:var(--sky)}
.bottom{left:0;top:1182px;width:873px;height:18px;background:var(--ice);text-align:center;font-size:5.5px;line-height:18px;color:#333}
</style>
</head>
<body>
<div class="page">

  <div class="abs hero" role="img" aria-label="Photo of a student wearing headphones around the neck, warm orange light with soft bokeh"></div>
  <div class="abs logo">LecternHop</div>
  <nav class="abs nav">
    <span class="active">Home</span><span>My Classes</span><span>Tools</span><span>Contact LecternHop</span><span>Shuffle Pick</span><span>The Grabber</span><span>Extra Tambourine</span>
  </nav>
  <div class="abs welcome">
    <h1>Welcome to LecternHop!</h1>
    <p>A collection of some fun and easy-to-use tools for building classroom communities and enabling active learning</p>
    <span class="btn">Sign Up</span>
  </div>

  <h2 class="abs section-title" style="top:318px">How we works</h2>
  <p class="abs intro">Lorem Ipsum is simply dummy text of the printing and typesetting industry. Lorem Ipsum has been the industry's standard dummy text ever since the 1500s, when an unknown printer took a galley of type and scrambled it to make a type specimen book. It has survived not only five centuries, but also the leap into electronic typesetting, remaining essentially unchanged</p>

  <h2 class="abs section-title" style="top:406px">Program</h2>

  <div class="abs card" style="left:181px;top:474px">
    <div class="badge"><svg width="30" height="30" viewBox="0 0 30 30"><circle cx="13" cy="13" r="11" fill="var(--sky)"/><circle cx="13" cy="13" r="3" fill="var(--ice)"/><rect x="18" y="16" width="9" height="11" rx="2" fill="var(--sky)"/></svg></div>
    <h3>Shuffle Pick</h3>
    <p>Where it all started! Students create playlists of upbeat music with TuneStream. At the start of class, one lucky student gets to be the class DJ. Typically paired with a “fib or fact” or “two truths and a lie” clicker activity.</p>
    <span class="btn">Read More</span>
  </div>
  <div class="abs card" style="left:310px;top:474px">
    <div class="badge"><svg width="30" height="30" viewBox="0 0 30 30"><rect x="8" y="3" width="14" height="24" rx="2" fill="var(--sky)"/><path d="M16 7 L11 16 H15 L13 23 L19 13 H15 Z" fill="var(--white)"/></svg></div>
    <h3>Flashcards</h3>
    <p>Get to know each other! With Flashcards you can “flip” through student (and instructor) profiles, learn names, and a little bit about what makes them tick. A great first step for creating an interactive classroom community.</p>
    <span class="btn">Read More</span>
  </div>
  <div class="abs card" style="left:439px;top:474px">
    <div class="badge"><svg width="30" height="30" viewBox="0 0 30 30"><path d="M15 2 V11 M15 11 C8 14 7 22 9 27 M15 11 C22 14 23 22 21 27" stroke="var(--brand)" stroke-width="2.5" fill="none" stroke-linecap="round"/></svg></div>
    <h3>"The Grabber"</h3>
    <p>The grabber chooses who will go and who will stay...well it randomly chooses a student from the class roster anyway. It's a fun way to encourage participation among quieter students and motivate active learning exercises.</p>
    <span class="btn">Read More</span>
  </div>
  <div class="abs card" style="left:568px;top:474px">
    <div class="badge"><svg width="30" height="30" viewBox="0 0 30 30"><rect x="10" y="2" width="10" height="26" rx="1" fill="var(--sky)"/><rect x="13" y="6" width="4" height="3" fill="var(--white)"/><rect x="13" y="11" width="4" height="3" fill="var(--white)"/><rect x="13" y="16" width="4" height="3" fill="var(--white)"/><rect x="13" y="21" width="4" height="3" fill="var(--white)"/></svg></div>
    <h3>Virtual Clicker</h3>
    <p>(coming soon) A simple tool for in-class polling. Launch multiple-choice questions from lecternhop.com or slides. Students respond via their laptop or smart phone. Bar graphs of the results (with “grabber” capabilities) link to student profiles.</p>
    <span class="btn">Read More</span>
  </div>

  <div class="abs card" style="left:181px;top:692px">
    <div class="badge"><svg width="30" height="30" viewBox="0 0 30 30"><path d="M9 4 H21 L26 25 H4 Z" fill="var(--sky)"/></svg></div>
    <h3 class="tight">Extra Tambourine</h3>
    <p>Sometimes the think-pair-share discussions get so feverish the only prescription is extra tambourine. In other words, when the class gets too noisy you can ring this virtual bell to get everyone's attention.</p>
    <span class="btn">Read More</span>
  </div>
  <div class="abs card" style="left:310px;top:692px">
    <div class="badge"><svg width="32" height="30" viewBox="0 0 32 30"><rect x="2" y="5" width="28" height="20" rx="1" fill="none" stroke="var(--sky)" stroke-width="2"/><circle cx="10" cy="12" r="3" fill="var(--sky)"/><path d="M5 21 C6 16 14 16 15 21 Z" fill="var(--sky)"/><rect x="18" y="10" width="9" height="2" fill="var(--sky)"/><rect x="18" y="15" width="9" height="2" fill="var(--sky)"/></svg></div>
    <h3>Student Profiles</h3>
    <p>Instructor-customizable profiles let students share information about themselves with the class. Use it to find out what students expect to learn, their previous coursework, or just to help people get to know each other (see flashcards).</p>
    <span class="btn">Read More</span>
  </div>
  <div class="abs card" style="left:439px;top:692px">
    <div class="badge"><svg width="30" height="30" viewBox="0 0 30 30"><rect x="4" y="7" width="20" height="20" fill="none" stroke="var(--sky)" stroke-width="3"/><path d="M9 16 L14 21 L27 5" stroke="var(--brand)" stroke-width="3.5" fill="none"/></svg></div>
    <h3>Self/Peer Evals</h3>
    <p>(coming Spring 2016) Self/Peer evaluations are a fantastic way to help students master material and deliver high quality feedback - fast. Works great in both large and small classes for either regular assignments or exams</p>
    <span class="btn">Read More</span>
  </div>
  <div class="abs card" style="left:568px;top:692px">
    <div class="badge"><svg width="32" height="28" viewBox="0 0 32 28"><rect x="2" y="3" width="28" height="22" fill="var(--sky)"/><g stroke="var(--ice)" stroke-width="1.5"><path d="M2 9H30M2 14H30M2 19H30M8 3V25M14 3V25M20 3V25M26 3V25"/></g></svg></div>
    <h3>Rubrics</h3>
    <p>(coming Spring 2016) Rubrics are a great tool - both for providing guidance and feedback. This tool lets you create your own rubrics to use for assignments (self/peer evals for example). Also, you can search a database of existing rubrics to use as a starting point.</p>
    <span class="btn">Read More</span>
  </div>

  <div class="abs band"></div>
  <div class="abs quote-card">
    <h2>What are Students Say</h2>
    <div class="abs avatar" role="img" aria-label="Portrait photo of the student giving the testimonial"></div>
    <div class="abs name">Dana Whitfield</div>
    <p class="abs text">Lorem Ipsum is simply dummy text of the printing and typesetting industry. Lorem Ipsum has been the industry's standard dummy text ever since the 1500s, when an unknown printer took a galley of type and scrambled it to make a type</p>
    <svg class="abs" style="left:440px;top:92px" width="36" height="30" viewBox="0 0 36 30"><path d="M2 30 V14 C2 6 7 2 14 2 V7 C10 8 9 11 9 14 H15 V30 Z M20 30 V14 C20 6 25 2 32 2 V7 C28 8 27 11 27 14 H34 V30 Z" fill="var(--ice)"/></svg>
  </div>
  <div class="abs dots"><span></span><span class="on"></span><span></span></div>

  <div class="abs foot-title" style="left:181px;top:1078px">Site Mape</div>
  <ul class="abs sitemap">
    <li>Home</li><li>My Classes</li><li>Tools</li><li>Contact LecternHop</li><li>Shuffle Pick</li><li>The Grabber</li><li>Extra Tambourine</li>
  </ul>

  <div class="abs foot-title" style="left:344px;top:1078px">Join LecternHop</div>
  <div class="abs join-lead">Join LecternHop for<br>get Education</div>
  <div class="abs email">Enter Email</div>
  <div class="abs btn join-btn">Sing Up</div>

  <div class="abs foot-title" style="left:534px;top:1078px">Contact Us</div>
  <div class="abs contact" style="top:1102px"><svg width="8" height="8" viewBox="0 0 10 10"><path d="M2 1 L4 1 L5 3 L4 4 C5 6 6 7 7 7 L8 6 L10 7 L10 9 C6 10 0 4 1 1 Z" fill="var(--brand)"/></svg>0800-555-0199</div>
  <div class="abs contact" style="top:1121px"><svg width="8" height="6" viewBox="0 0 10 7"><rect width="10" height="7" fill="var(--brand)"/><path d="M0 0 L5 4 L10 0" stroke="var(--white)" fill="none"/></svg>info@lecternhop.com</div>
  <div class="abs social"><span></span><span></span><span></span></div>

  <div class="abs bottom">© 2016 LecternHop</div>
</div>
</body>
</html>
```